Email signature design - law firm

We are a small boutique law firm which is located near the beach in Manly, Australia.

We have just recently developed a new logo and are looking to redesign our letterhead, business cards and email signatures.

This brief is for our email signatures. This is an email signature to appear at the bottom of our Outlook emails so we would like it to be text that we are able to edit as the wording in our email signature often required amendments.

I have attached a word document which had our new logo, and our previous email signature which all the information/wording that needs to be included.

We would like multiple designs with a modern, simplistic yet striking look.

Thanks.

font - raleway or montserrat

Need extra days to review

• Must have the exact wording which appears in the email signature in the word document attached to brief.
• Must be able to edit the text as it is for an Outlook email signature which wording will change from time to time.

```html
<!DOCTYPE html>
<html lang="en">
<head>
<meta charset="utf-8">
<title>Harbourne &amp; Partners – Letterhead and Email Signature</title>
<link rel="stylesheet" href="https://fonts.googleapis.com/css2?family=Lato:wght@400;700&display=swap">
<style>
  :root {
    --backdrop: #262626;
    --paper: #ffffff;
    --navy: #2e3a87;
    --gold: #b9a469;
    --sky: #7b8fcc;
    --ink: #1f1f1f;
  }
  * { margin: 0; padding: 0; box-sizing: border-box; }
  html, body { width: 800px; height: 1200px; overflow: hidden; }
  body {
    background: var(--backdrop);
    font-family: "Lato", sans-serif;
    position: relative;
  }
  .letterhead, .signature {
    position: absolute;
    left: 146px;
    width: 509px;
    background: var(--paper);
  }
  .letterhead { top: 117px; height: 762px; }
  .signature { top: 966px; height: 153px; }

  .brand {
    position: absolute;
    display: flex;
    align-items: center;
    gap: 6px;
    font-weight: 700;
    color: var(--navy);
    white-space: nowrap;
  }
  .brand-dot {
    width: 9px; height: 9px; border-radius: 50%;
    background: var(--gold);
  }
  .letterhead .brand { top: 42px; left: 0; right: 0; justify-content: center; font-size: 14px; }
  .signature .brand { top: 42px; right: 34px; font-size: 10px; }
  .signature .brand-dot { width: 7px; height: 7px; }

  .office-line {
    position: absolute;
    top: 713px; left: 84px;
    font-size: 10.5px;
    color: var(--ink);
    white-space: nowrap;
  }
  .office-line .firm { color: var(--navy); }

  .contact-band { position: absolute; left: 0; width: 100%; }
  .letterhead .contact-band { top: 735px; height: 27px; }
  .signature .contact-band { top: 132px; height: 21px; }
  .contact-band svg { position: absolute; inset: 0; width: 100%; height: 100%; }
  .band-navy { fill: var(--navy); }
  .band-gold { fill: var(--gold); }
  .band-sky { fill: var(--sky); }
  .band-item {
    position: absolute; top: 0; bottom: 0;
    display: flex; align-items: center;
    color: #ffffff;
    white-space: nowrap;
  }
  .letterhead .band-item { font-size: 10.5px; }
  .signature .band-item { font-size: 11.5px; }
  .letterhead .phone { left: 31px; }
  .letterhead .fax { left: 176px; }
  .letterhead .web { left: 321px; }
  .signature .phone { left: 39px; }
  .signature .fax { left: 165px; }
  .signature .web { left: 283px; }

  .sign-off { position: absolute; top: 27px; left: 39px; }
  .sign-off .greeting { font-size: 12px; color: var(--ink); line-height: 14px; }
  .sign-off .person { font-size: 15px; font-weight: 700; color: var(--navy); line-height: 18px; }
  .sign-address { position: absolute; top: 91px; left: 37px; font-size: 12px; line-height: 15px; }
  .sign-address .firm { color: var(--navy); }
  .sign-address .street { color: var(--ink); }
</style>
</head>
<body>

<section class="letterhead">
  <div class="brand"><span class="brand-dot"></span>Harbourne &amp; Partners</div>

  <p class="office-line"><span class="firm">HARBOURNE &amp; PARTNERS:</span>&nbsp; Suite 4, 12 Pier Lane, MANLY&nbsp;&nbsp;&nbsp; NSW&nbsp;&nbsp; 2095</p>

  <div class="contact-band">
    <svg viewBox="0 0 509 27" preserveAspectRatio="none">
      <path class="band-navy" d="M0 0 H156 Q149 12 150 27 H0 Z"/>
      <path class="band-gold" d="M161 0 H299 Q292 12 293 27 H154 Q153 12 161 0 Z"/>
      <path class="band-sky" d="M304 0 H509 V27 H297 Q296 12 304 0 Z"/>
    </svg>
    <span class="band-item phone">P: (02) 9000 4182</span>
    <span class="band-item fax">F: (02) 9000 4183</span>
    <span class="band-item web">www.harbourneandpartners.com.au</span>
  </div>
</section>

<section class="signature">
  <div class="sign-off">
    <p class="greeting">Regards</p>
    <p class="person">Nadia Ellison</p>
  </div>

  <div class="brand"><span class="brand-dot"></span>Harbourne &amp; Partners</div>

  <div class="sign-address">
    <p class="firm">Harbourne &amp; Partners:</p>
    <p class="street">Suite 4, 12 Pier Lane, MANLY&nbsp; NSW&nbsp; 2095</p>
  </div>

  <div class="contact-band">
    <svg viewBox="0 0 509 21" preserveAspectRatio="none">
      <path class="band-navy" d="M0 0 H153 Q147 10 148 21 H0 Z"/>
      <path class="band-gold" d="M158 0 H276 Q270 10 271 21 H151 Q151 10 158 0 Z"/>
      <path class="band-sky" d="M281 0 H509 V21 H274 Q274 10 281 0 Z"/>
    </svg>
    <span class="band-item phone">P: (02) 9000 4182</span>
    <span class="band-item fax">F: (02) 9000 4183</span>
    <span class="band-item web">www.harbourneandpartners.com.au</span>
  </div>
</section>

</body>
</html>
```